Trade show post card for sportfishing

I would like a double sided postcard used to be a larger more descriptive, eye catching, marketing tool to be used at trade show. I want the double sided postcard to be descriptive and eye catching for both avid fisherman and inviting enough not to scare away first timers looking to enjoy the experience.

Target Market(s)

Males 25-60

Colors

Designer to choose colors to be used in the design.

Requirements
Must have
• My logo, website, phone number, type of trips, pictures of fishing trips we have had which I included below. But I do not need all of the pictures designers can use ones they feel will be most appealing
Nice to have
• Color scheme that works with my logo.

```html
<!DOCTYPE html>
<html lang="en">
<head>
<meta charset="utf-8">
<title>Slack Tide Charters – Postcard Back</title>
<link href="https://fonts.googleapis.com/css2?family=Arimo:wght@400;700&family=Mulish:wght@500&family=Roboto+Condensed:wght@400;700&display=swap" rel="stylesheet">
<style>
  :root {
    --ink: #000000;
    --lime: #77d53c;
    --forest: #377107;
    --white: #ffffff;
    --slate: #5f6b6d;
    --page: #ffffff;
    --photo-a: #8aa0a8;
    --photo-b: #d9dedf;
  }
  * { margin: 0; padding: 0; box-sizing: border-box; }
  html, body { width: 1200px; height: 960px; overflow: hidden; background: var(--page); }
  .canvas { position: relative; width: 1200px; height: 960px; }

  .top-band {
    position: absolute; left: 36px; top: 59px; width: 1128px; height: 96px;
    background: var(--ink); display: flex; align-items: center; padding-left: 52px;
  }
  .top-band__title { font-family: "Arimo", sans-serif; font-weight: 700; font-size: 28.5px; color: var(--lime); letter-spacing: 0.2px; }
  .top-band__sub { font-family: "Mulish", sans-serif; font-weight: 500; font-size: 25px; color: var(--white); margin-left: 29px; }

  .features {
    position: absolute; left: 36px; top: 155px; width: 608px; height: 557px; background: var(--lime);
  }
  .feature { position: absolute; left: 0; width: 608px; }
  .feature__icon { position: absolute; left: 38px; width: 52px; height: 52px; }
  .feature__text {
    position: absolute; left: 116px; width: 480px;
    font-family: "Mulish", sans-serif; font-weight: 500; font-size: 21px; line-height: 27px; color: var(--ink);
  }

  .photo {
    position: absolute; left: 644px; top: 155px; width: 520px; height: 275px;
    background: linear-gradient(180deg, var(--photo-b) 0%, var(--photo-a) 55%, #c9cfcf 100%);
  }

  .boat-panel {
    position: absolute; left: 644px; top: 430px; width: 520px; height: 282px;
    background: var(--forest); color: var(--white); text-align: center;
    font-family: "Roboto Condensed", sans-serif;
  }
  .boat-panel__desc { position: absolute; top: 20px; left: 0; width: 520px; font-weight: 700; font-size: 22.5px; line-height: 31px; }
  .boat-panel__guests { position: absolute; top: 150px; left: 0; width: 520px; font-family: "Arimo", sans-serif; font-weight: 700; font-size: 32px; }
  .boat-panel__note { position: absolute; top: 190px; left: 0; width: 520px; font-size: 21px; }

  .contact-band {
    position: absolute; left: 36px; top: 712px; width: 1128px; height: 98px; background: var(--ink);
    font-size: 28px; color: var(--white);
  }
  .contact-band__label { position: absolute; top: 32px; font-family: "Arimo", sans-serif; font-weight: 700; color: var(--lime); }
  .contact-band__value { position: absolute; top: 32px; font-family: "Mulish", sans-serif; font-weight: 500; }

  .side-label {
    position: absolute; left: 0; top: 846px; width: 1200px; text-align: center;
    font-family: "Arimo", sans-serif; font-weight: 700; font-size: 52px; color: var(--slate);
  }
</style>
</head>
<body>
<div class="canvas">
  <header class="top-band">
    <span class="top-band__title">HALF OR FULL DAY CHARTERS</span>
    <span class="top-band__sub">April and May sailing from Poughkeepsie, NY</span>
  </header>

  <section class="features">
    <div class="feature" style="top:47px">
      <svg class="feature__icon" style="top:2px" viewBox="0 0 52 52">
        <circle cx="26" cy="26" r="25" fill="var(--ink)"/>
        <circle cx="15" cy="20" r="3.2" fill="var(--lime)"/>
        <circle cx="26" cy="12" r="3.2" fill="var(--lime)"/>
        <circle cx="38" cy="20" r="3.2" fill="var(--lime)"/>
        <circle cx="38" cy="33" r="3.2" fill="var(--lime)"/>
        <line x1="24" y1="24" x2="44" y2="47" stroke="var(--lime)" stroke-width="5" stroke-linecap="round"/>
        <line x1="24" y1="24" x2="44" y2="47" stroke="var(--ink)" stroke-width="2" stroke-linecap="round"/>
        <circle cx="48" cy="51" r="4" fill="var(--ink)"/>
      </svg>
      <p class="feature__text" style="top:8px">Slack Tide has top of the line custom made fishing rods paired with brightwater reels for your use.</p>
    </div>

    <div class="feature" style="top:163px">
      <svg class="feature__icon" viewBox="0 0 52 52">
        <circle cx="26" cy="26" r="25" fill="var(--ink)"/>
        <path d="M26 40 C20 31 17 26 17 21 a9 9 0 0 1 18 0 c0 5 -3 10 -9 19z" fill="var(--lime)"/>
        <circle cx="26" cy="21" r="3.5" fill="var(--ink)"/>
      </svg>
      <p class="feature__text" style="top:16px">We have the best electronics on the market by Norwave to maximize our fish finding capability and safe navigation.</p>
    </div>

    <div class="feature" style="top:289px">
      <svg class="feature__icon" viewBox="0 0 52 52">
        <circle cx="26" cy="26" r="25" fill="var(--ink)"/>
        <circle cx="26" cy="26" r="11" fill="none" stroke="var(--lime)" stroke-width="3"/>
        <circle cx="26" cy="26" r="3" fill="var(--lime)"/>
        <path d="M26 8v9M26 35v9M8 26h9M35 26h9" stroke="var(--lime)" stroke-width="3"/>
      </svg>
      <p class="feature__text" style="top:16px">Targeting Striped Bass during their spring migration up the Hudson River</p>
    </div>

    <div class="feature" style="top:417px">
      <svg class="feature__icon" viewBox="0 0 52 52">
        <circle cx="26" cy="26" r="25" fill="var(--ink)"/>
        <path d="M12 20 L19 29 L26 17 L33 29 L40 20 L37 34 H15z" fill="var(--lime)"/>
        <rect x="15" y="36" width="22" height="3.5" fill="var(--lime)"/>
      </svg>
      <p class="feature__text" style="top:14px">Captain Dan Harlow is a USCG Licensed Captain with over 25 years of experience.</p>
    </div>
  </section>

  <div class="photo" role="img" aria-label="Photo: five anglers on a charter boat at the dock holding striped bass"></div>

  <section class="boat-panel">
    <p class="boat-panel__desc">Come aboard our 27 foot Kestrel, powered by<br>twin 200 Horsepower engines with a working<br>head, cabin, and full enclosure.</p>
    <p class="boat-panel__guests">1-4 GUESTS</p>
    <p class="boat-panel__note">KID &amp; BEGINNER FRIENDLY</p>
  </section>

  <footer class="contact-band">
    <span class="contact-band__label" style="left:110px">CALL</span>
    <span class="contact-band__value" style="left:206px">845 - 555 - 0193</span>
    <span class="contact-band__label" style="left:513px">EMAIL</span>
    <span class="contact-band__value" style="left:626px">slacktidefish@mailbox.com</span>
  </footer>

  <p class="side-label">BACK</p>
</div>
</body>
</html>
```